Invitation Design Project

I need a customized graphic design for my wedding invitation.I want it to be non-traditional wedding invite. The design in mind is like a movie poster graphics while adopting 'the bright days on the islands' font style and colors that create a light mood at the front page.Inside pages can be similar to movie posters with dark background similar to that of Grey harbor.Wedding related art/graphics can be integrated within the design.Wordings can be discussed later.

Industry/Entity Type

Graphic Design

Requirements
Must have
• Other must have features are our pictures as couple which will be sent .
Nice to have
• we would like to have the words

"our wedding.

more fun if you'll come!"

on the front cover.

```html
<!DOCTYPE html>
<html lang="en">
<head>
<meta charset="utf-8">
<title>Our Wedding – Invitation Layout</title>
<link rel="stylesheet" href="https://fonts.googleapis.com/css2?family=Lobster+Two:ital,wght@1,700&family=Arimo:wght@400&display=swap">
<style>
  :root {
    --paper: #ffffff;
    --blush: #dc98a3;
    --ink: #1e1a1b;
    --label: #111111;
    --script: "Lobster Two", cursive;
    --sans: "Arimo", Arial, sans-serif;
  }
  * { margin: 0; padding: 0; box-sizing: border-box; }
  html, body { width: 1200px; height: 900px; overflow: hidden; background: var(--paper); }
  .sheet { position: relative; width: 1200px; height: 900px; }

  .panel { position: absolute; overflow: hidden; }
  .panel svg.frame { position: absolute; inset: 0; width: 100%; height: 100%; }
  .script { font-family: var(--script); font-style: italic; font-weight: 700; text-align: center; position: absolute; left: 0; right: 0; }

  .view-label { position: absolute; font-family: var(--sans); font-size: 40px; color: var(--label); text-align: center; line-height: 1; }

  .portrait { position: absolute; }
  .ornament { position: absolute; }

  /* front cover */
  .front { left: 36px; top: 36px; width: 265px; height: 376px; background: var(--blush); }
  .front .title { top: 50px; font-size: 26px; letter-spacing: 1px; color: var(--ink); }
  .front .tagline { top: 342px; font-size: 14px; color: var(--ink); }
  .front .portrait { left: 56px; top: 136px; width: 184px; height: 186px;
    background: radial-gradient(ellipse at 50% 45%, var(--ink) 0%, #3a2a2d 55%, var(--blush) 80%); }

  /* middle spread */
  .spread { left: 335px; top: 236px; width: 530px; height: 375px; }
  .spread .leaf { position: absolute; top: 0; width: 265px; height: 375px; }
  .spread .leaf-left { left: 0; background: var(--ink); color: var(--blush); }
  .spread .leaf-right { left: 265px; background: var(--blush); color: var(--ink); }
  .spread .script { font-size: 15px; line-height: 22px; }
  .leaf-left .hosts { top: 62px; line-height: 21px; }
  .leaf-left .invite { top: 134px; }
  .leaf-right .reception { top: 62px; }
  .leaf-right .rsvp { top: 203px; }

  /* back */
  .back { left: 889px; top: 399px; width: 261px; height: 371px; background: var(--blush); }
  .back .portrait { left: 38px; top: 14px; width: 200px; height: 178px;
    background: radial-gradient(ellipse at 55% 45%, var(--ink) 0%, #3a2a2d 55%, var(--blush) 82%); }
  .back .note { top: 220px; font-size: 13px; color: var(--ink); }
</style>
</head>
<body>
<main class="sheet">

  <section class="panel front" aria-label="Front cover">
    <svg class="frame" viewBox="0 0 265 376" aria-hidden="true">
      <line x1="54" y1="16" x2="265" y2="16" stroke="#1e1a1b" stroke-width="3"/>
      <line x1="12" y1="58" x2="12" y2="376" stroke="#1e1a1b" stroke-width="3"/>
    </svg>
    <div class="ornament" role="img" aria-label="Swirl corner ornament" style="left:6px;top:4px;width:50px;height:28px;background:#1e1a1b;opacity:.55;border-radius:14px 14px 14px 2px;"></div>
    <h1 class="script title">our wedding</h1>
    <div class="portrait" role="img" aria-label="Stencil portrait of the couple"></div>
    <p class="script tagline">more fun if you’ll come!</p>
  </section>
  <p class="view-label" style="left:95px;top:434px;width:115px;">front</p>

  <section class="panel spread" aria-label="Middle spread">
    <div class="leaf leaf-left">
      <svg class="frame" viewBox="0 0 265 375" aria-hidden="true">
        <line x1="60" y1="20" x2="265" y2="20" stroke="#dc98a3" stroke-width="3"/>
        <line x1="9" y1="54" x2="9" y2="361" stroke="#dc98a3" stroke-width="3"/>
        <line x1="9" y1="361" x2="265" y2="361" stroke="#dc98a3" stroke-width="3"/>
      </svg>
      <div class="ornament" role="img" aria-label="Swirl corner ornament" style="left:8px;top:20px;width:56px;height:22px;background:#dc98a3;opacity:.6;border-radius:12px;"></div>
      <p class="script hosts">Mr &amp; Mrs Last Name<br>&amp;<br>Mr &amp; Mrs Last Name</p>
      <p class="script invite">invite you to join<br>them in celebrating<br>the marriage of<br>name and name<br>at location<br>date<br>time</p>
      <div class="ornament" role="img" aria-label="Small flourish ornament" style="left:96px;top:328px;width:74px;height:14px;background:#dc98a3;opacity:.75;border-radius:50% 50% 40% 40%;"></div>
    </div>
    <div class="leaf leaf-right">
      <svg class="frame" viewBox="0 0 265 375" aria-hidden="true">
        <line x1="0" y1="20" x2="247" y2="20" stroke="#1e1a1b" stroke-width="3"/>
        <line x1="247" y1="20" x2="247" y2="340" stroke="#1e1a1b" stroke-width="3"/>
        <line x1="0" y1="361" x2="190" y2="361" stroke="#1e1a1b" stroke-width="3"/>
      </svg>
      <p class="script reception">Reception to follow at<br>time<br>location<br>address</p>
      <p class="script rsvp">Please RSVP by<br>day month year<br>email address<br>phone number</p>
      <div class="ornament" role="img" aria-label="Small flourish ornament" style="left:96px;top:328px;width:74px;height:14px;background:#1e1a1b;opacity:.75;border-radius:50% 50% 40% 40%;"></div>
      <div class="ornament" role="img" aria-label="Swirl corner ornament" style="left:196px;top:338px;width:56px;height:22px;background:#1e1a1b;opacity:.55;border-radius:12px;"></div>
    </div>
  </section>
  <p class="view-label" style="left:430px;top:642px;width:340px;">middle spread</p>

  <section class="panel back" aria-label="Back cover">
    <svg class="frame" viewBox="0 0 261 371" aria-hidden="true">
      <line x1="242" y1="0" x2="242" y2="330" stroke="#1e1a1b" stroke-width="3"/>
      <line x1="0" y1="353" x2="172" y2="353" stroke="#1e1a1b" stroke-width="3"/>
    </svg>
    <div class="portrait" role="img" aria-label="Stencil portrait of the couple"></div>
    <p class="script note">more text</p>
    <div class="ornament" role="img" aria-label="Swirl corner ornament" style="left:172px;top:330px;width:62px;height:26px;background:#1e1a1b;opacity:.55;border-radius:14px 14px 2px 14px;"></div>
  </section>
  <p class="view-label" style="left:985px;top:812px;width:116px;">back</p>

</main>
</body>
</html>
```